Software company design for letters and quotations

Clean modern design. Colors & logo are available on our website.
www.tralvexsoft.be

Target Market(s)

business clients

Industry/Entity Type

Business Software

Requirements
Must have
• delivery as word templates & psd

```html
<!DOCTYPE html>
<html lang="en">
<head>
<meta charset="utf-8">
<title>Tralvex Soft – Letterhead</title>
<link href="https://fonts.googleapis.com/css2?family=Roboto+Condensed:wght@400&family=PT+Sans:wght@400&display=swap" rel="stylesheet">
<style>
  :root {
    --brand-blue: #0f5f87;
    --ink: #1e1e1e;
    --ink-soft: #333333;
    --paper: #ffffff;
    --backdrop: #e9e7e3;
  }
  * { margin: 0; padding: 0; box-sizing: border-box; }
  html, body {
    width: 1189px; height: 1200px; overflow: hidden;
    background: var(--backdrop);
  }
  .letterhead {
    position: absolute; left: 131px; top: 0;
    width: 927px; height: 1200px;
    background: var(--paper);
  }
  .company-name {
    position: absolute; left: 76px; top: 104px;
    font-family: "PT Sans", sans-serif; font-weight: 400;
    font-size: 44px; line-height: 56px;
    color: var(--ink-soft);
  }
  .salutation {
    position: absolute; left: 118px; top: 230px;
    font-family: "PT Sans", sans-serif; font-size: 22px;
    color: var(--ink-soft);
  }
  .letter-body {
    position: absolute; left: 120px; top: 278px; width: 690px;
    font-family: "Roboto Condensed", "Arial Narrow", sans-serif;
    font-size: 18.4px; line-height: 27.3px; color: var(--ink);
    hyphens: auto; -webkit-hyphens: auto;
  }
  .letter-body p { margin-bottom: 27.3px; }
  .letter-body p.gap-after { margin-bottom: 54.6px; }
  .footer-rule {
    position: absolute; left: 79px; top: 1089px;
    width: 768px; height: 6px; background: var(--brand-blue);
  }
  .contact {
    position: absolute; top: 1108px; left: 79px; width: 768px;
    font-family: "PT Sans", sans-serif; font-size: 16.5px;
    line-height: 19.5px; color: var(--ink-soft);
  }
  .contact-col { position: absolute; top: 0; }
  .contact-col.phones { left: 0; }
  .contact-col.online { left: 291px; }
  .contact-col.address { left: 588px; }
  .contact-line { display: flex; align-items: center; gap: 5px; white-space: nowrap; }
  .contact-line svg { width: 13px; height: 13px; flex: none; }
  .divider {
    position: absolute; top: 2px; width: 2px; height: 36px;
    background: var(--ink-soft);
  }
  .divider.first { left: 229px; }
  .divider.second { left: 535px; }
</style>
</head>
<body>
<main class="letterhead">
  <header class="company-name">Tralvex Soft</header>

  <p class="salutation">Dear Sir</p>

  <section class="letter-body">
    <p>Lorem Ipsum is simply dummy text of the printing and typesetting industry. Lorem Ipsum has been the industry’s standard dummy text ever since the 1500s, when an unknown printer took a galley of type and scrambled it to make a type specimen book. It has survived not only five centuries, but also the leap into electronic typesetting, remaining essentially unchanged. It was popularised in the 1960s with the release of Lettrafix sheets containing Lorem Ipsum passages, and more recently with desktop publishing software like Pagewright Studio including versions of Lorem Ipsum.</p>
    <p class="gap-after">It is a long established fact that a reader will be distracted by the readable content of a page when looking at its layout. The point of using Lorem Ipsum is that it has a more-or-less normal distribution of letters, as opposed to using ’Content here, content here’, making it look like readable English. Many desktop publishing packages and web page editors now use Lorem Ipsum as their default model text, and a search for ’lorem ipsum’ will uncover many web sites still in their infancy. Various versions have evolved over the years, sometimes by accident, sometimes on purpose (injected humour and the like).</p>
    <p>Contrary to popular belief, Lorem Ipsum is not simply random text. It has roots in a piece of classical Latin literature from 45 BC, making it over 2000 years old. Robert Hallsworth, a Latin professor at Ashcombe College in Virginia, looked up one of the more obscure Latin words, consectetur, from a Lorem Ipsum passage, and going through the cites of the word in classical literature, discovered the undoubtable source. Lorem Ipsum comes from sections 1.10.32 and 1.10.33 of "de Finibus Bonorum et Malorum" structures, to generate Lorem Ipsum which looks reasonable. The generated Lorem Ipsum is therefore always free from repetition, injected humour, or non-characteristic words etc.</p>
  </section>

  <div class="footer-rule"></div>

  <footer class="contact">
    <div class="contact-col phones">
      <div class="contact-line">
        <svg viewBox="0 0 13 13" aria-hidden="true"><rect width="13" height="13" rx="1.5" fill="var(--brand-blue)"/><path d="M4 3c-.8.5-1 1.4-.6 2.4.8 2 2.2 3.5 4.2 4.3 1 .4 1.9.1 2.4-.7l-1.6-1.3-.9.7c-1-.5-1.8-1.3-2.3-2.3l.7-.9z" fill="#fff"/></svg>
        <span>+32(0)3555.12.40</span>
      </div>
      <div class="contact-line">
        <svg viewBox="0 0 13 13" aria-hidden="true"><rect width="13" height="13" rx="1.5" fill="var(--brand-blue)"/><rect x="3" y="2.5" width="7" height="3" fill="#fff"/><rect x="2.5" y="6.5" width="8" height="4" fill="#fff"/></svg>
        <span>+00(0)0000.00.00</span>
      </div>
    </div>
    <div class="divider first"></div>
    <div class="contact-col online">
      <div class="contact-line">
        <svg viewBox="0 0 13 13" aria-hidden="true"><rect width="13" height="13" rx="1.5" fill="var(--brand-blue)"/><rect x="2.5" y="3.5" width="8" height="6" fill="#fff"/><path d="M2.5 3.5l4 3.2 4-3.2" stroke="var(--brand-blue)" fill="none"/></svg>
        <span>info@tralvexsoft.be</span>
      </div>
      <div class="contact-line">
        <svg viewBox="0 0 13 13" aria-hidden="true"><rect width="13" height="13" rx="1.5" fill="var(--brand-blue)"/><circle cx="6.5" cy="6.5" r="4" fill="none" stroke="#fff"/><path d="M2.5 6.5h8M6.5 2.5v8" stroke="#fff"/></svg>
        <span>www.tralvexsoft.be</span>
      </div>
    </div>
    <div class="divider second"></div>
    <div class="contact-col address">
      <div class="contact-line"><span>Kaaistraat 14</span></div>
      <div class="contact-line"><span>2000 Antwerpen, België</span></div>
    </div>
  </footer>
</main>
</body>
</html>
```